intraoral tooth cleaning device requires JAZZY NEW PACKAGING

I already have a logo design for my product "GUMBRA" but I need a sharply designed packaging. Something that is bright and stands out.
Gumbra is an anatomically and ergonomically correct dental plaque remover. It
"Makes Every Smile Brightly Fresh".
Go to my website gumbrapick.example to get the logo design and the look and feel of the product. Also there is more information about the product.
I am trying to get a package with 10 pieces of Gumbra in each package. I also would be interested in packaging for 20 pieces also..I would like the package to be like a pack of cigarettes and fit in a shirt pocket.
Colors used should be green, white, yellow, blue. Clean pharmaceutical looking.
The Gumbra is easy to use, only one hand required and it is reusable.
On you tube I have 2 videos listed under "gumbra hd" Watch them for more info.
I am sending more variations of the "GUMBRA" logo that I have designed. They are very good variations.

Reason: Only have 5 responses. I thought there was to be at least 50.????

I am very sorry that I have not given any feed back. But there is a very good reason. I ALMOST DIED 4 TIMES.I was vomiting food on every meal and went through many tests to find the problem. It was determined that I had a diverticulum of the esophagus, or a bubble that if it had burst I would have died very quickly. I had a surgery on Feb 13, 2014 that was meant to fix this condition, But did not turn out very well for me. I have had 4 more surgeries since. I am doing much better now and I hope this last surgery will fix the problem. I again would like to apologize to all of the designers that submitted a design. Truly there was not much I could have done, I was fighting for my life. I would like to extend the date by an extra month from now if that is okay with all of the designers. You all have done a great job. And now that I have most of my energy back I can devote some time to completing this project. Most Respectfully Yours Dr. Martin L. Pelham

Target Market(s)

Anyone with teeth that gets food stuck in between them. Mostly adults , not really children, though I have my own kids who love them.

Industry/Entity Type

Dental

Requirements
Must have
• Clean, Healthy look and feel. A look that promotes health and well being.
• something pharmaceutical like. Clean colors blue,green, white, yellow.
Nice to have
• the advantages of Dr. designed, non-abrasive to tooth structure. Easy to use. Re-usable. Safe for dental implants.
Should not have
• old design, dark colors, i.e. browns, grays, nothing drab.

```html
<!DOCTYPE html>
<html lang="en">
<head>
<meta charset="utf-8">
<title>Gumbra Pack Front Panel</title>
<link rel="stylesheet" href="https://fonts.googleapis.com/css2?family=Oswald:wght@500&family=PT+Sans:wght@400;700&display=swap">
<style>
  :root {
    --stage: #2f4fa0;
    --band-top: #1c9fdc;
    --band-bottom: #1b57ab;
    --panel: #ffffff;
    --brand-blue: #1c4fa3;
    --brand-green: #1f9a48;
    --copy-blue: #1f3f9a;
    --teal-light: #1f8f86;
    --teal-dark: #17405f;
    --photo-light: #f7e9e4;
    --photo-mid: #e9b9ae;
    --photo-deep: #d9858a;
  }
  * { margin: 0; padding: 0; box-sizing: border-box; }
  html, body { width: 1200px; height: 1000px; overflow: hidden; }
  body {
    background: var(--stage);
    position: relative;
    font-family: "PT Sans", Arial, sans-serif;
  }
  .pack-front {
    position: absolute;
    left: 340px; top: 100px;
    width: 520px; height: 800px;
    background: var(--panel);
    overflow: hidden;
    box-shadow: 0 10px 30px rgba(0,0,0,.25);
  }
  .headline-band {
    height: 180px;
    background: linear-gradient(180deg, var(--band-top), var(--band-bottom));
    display: flex; align-items: center; justify-content: center;
    text-align: center;
    font-family: "Oswald", "Arial Narrow", sans-serif;
    font-weight: 500;
    color: #fff;
    font-size: 37px;
    line-height: 1.25;
    letter-spacing: .5px;
    padding: 0 30px;
  }
  .product-photo {
    position: absolute;
    left: 0; right: 0; top: 380px; bottom: 0;
    background: radial-gradient(ellipse at 45% 50%, var(--photo-deep) 0%, var(--photo-mid) 35%, var(--photo-light) 70%);
  }
  .brand-name {
    position: absolute;
    top: 218px; left: 0; right: 0;
    text-align: center;
    font-weight: 700;
    font-size: 92px;
    line-height: 1;
    letter-spacing: 4px;
    color: var(--brand-blue);
  }
  .tagline {
    position: absolute;
    top: 330px; left: 0; right: 0;
    text-align: center;
    font-size: 26px;
    color: var(--brand-green);
  }
  .benefits {
    position: absolute;
    top: 384px; left: 90px; right: 70px;
    list-style: none;
    text-align: center;
    font-size: 19px;
    line-height: 1.28;
    color: var(--copy-blue);
    z-index: 1;
  }
  .count-band {
    position: absolute;
    left: 40px; right: 40px; bottom: 0;
    height: 120px;
    border-radius: 34px 34px 0 0;
    background: linear-gradient(180deg, var(--teal-light), var(--teal-dark));
    display: flex; align-items: center; justify-content: center;
    color: #fff;
    font-weight: 700;
    font-size: 38px;
  }
</style>
</head>
<body>
  <section class="pack-front">
    <header class="headline-band">USING GUMBRA’S IS BENEFICIAL FOR HEALTHY TEETH AND GUMS</header>
    <div class="product-photo" role="img" aria-label="Close-up photograph of a smiling mouth with white teeth beside a dental mirror"></div>
    <div class="brand-name">GUMBRA</div>
    <p class="tagline">Makes Every Smile Brightly Fresh!™</p>
    <ul class="benefits">
      <li>Dr. designed.</li>
      <li>Non-abrasive to tooth structure.</li>
      <li>Easy to use.</li>
      <li>Re-usable.</li>
      <li>Safe for dental implants.</li>
    </ul>
    <div class="count-band">20 Gumbra’s</div>
  </section>
</body>
</html>
```